VitaLern
Lifeline Instruction
Simple
Ted Marwick
Owner
287 Felcourt Lane Ashbrook, Westmere 00417
Ted@VitaLern.com
www.VitaLern.com
Healthcare education and consulting.

```html
<!DOCTYPE html>
<html lang="en">
<head>
<meta charset="utf-8">
<title>VitaLern Business Card</title>
<link href="https://fonts.googleapis.com/css2?family=Roboto+Slab:wght@300;400;700&display=swap" rel="stylesheet">
<style>
  :root {
    --brand-red: #dc4b42;
    --card-white: #ffffff;
    --backdrop: #e4e4e4;
    --text-grey: #6f6f6f;
    --divider: #c9c9c9;
  }
  * { margin: 0; padding: 0; box-sizing: border-box; }
  html, body {
    width: 1200px;
    height: 901px;
    overflow: hidden;
    background: var(--backdrop);
    font-family: "Roboto Slab", Georgia, serif;
  }
  .canvas { position: relative; width: 1200px; height: 901px; }

  .card {
    position: absolute;
    left: 299px;
    width: 601px;
    height: 341px;
    border-radius: 16px;
    overflow: hidden;
  }

  /* Front side */
  .card-front { top: 68px; background: var(--brand-red); color: var(--card-white); }
  .front-name {
    position: absolute;
    top: 150px;
    left: 0;
    width: 100%;
    text-align: center;
    font-size: 60px;
    font-weight: 700;
    line-height: 1;
  }
  .front-tagline {
    position: absolute;
    top: 304px;
    left: 0;
    width: 100%;
    text-align: center;
    font-size: 14px;
    font-weight: 300;
  }

  /* Back side */
  .card-back { top: 487px; background: var(--card-white); }
  .brand {
    position: absolute;
    left: 34px;
    top: 142px;
    color: var(--brand-red);
  }
  .brand-row { display: flex; align-items: center; gap: 10px; }
  .brand-mark { width: 22px; height: 22px; background: var(--brand-red); }
  .brand-name { font-size: 28px; font-weight: 400; line-height: 1; }
  .brand-tagline { margin-top: 6px; margin-left: 32px; font-size: 16px; font-weight: 400; }

  .divider {
    position: absolute;
    left: 302px;
    top: 73px;
    width: 1px;
    height: 195px;
    background: var(--divider);
  }

  .details { position: absolute; left: 322px; top: 70px; color: var(--text-grey); }
  .person-name {
    color: var(--brand-red);
    font-size: 27px;
    font-weight: 700;
    letter-spacing: 0.5px;
    line-height: 1.1;
  }
  .person-role { font-size: 12px; margin-top: 4px; }
  .address { font-size: 15px; line-height: 20px; margin-top: 20px; }
  .contacts { list-style: none; margin-top: 14px; font-size: 14px; }
  .contacts li { display: flex; align-items: center; gap: 10px; height: 19.5px; }
  .contacts svg { width: 11px; height: 11px; fill: var(--brand-red); flex: none; }
</style>
</head>
<body>
<main class="canvas">
  <section class="card card-front" aria-label="Card front">
    <div class="front-name">VitaLern</div>
    <p class="front-tagline">Healthcare Education and Consulting</p>
  </section>

  <section class="card card-back" aria-label="Card back">
    <div class="brand">
      <div class="brand-row">
        <span class="brand-mark"></span>
        <span class="brand-name">VitaLern</span>
      </div>
      <p class="brand-tagline">Lifeline Instruction</p>
    </div>

    <div class="divider"></div>

    <div class="details">
      <h1 class="person-name">TED MARWICK</h1>
      <p class="person-role">Owner</p>
      <p class="address">287 Felcourt Lane Ashbrook,<br>Westmere 00417</p>
      <ul class="contacts">
        <li>
          <svg viewBox="0 0 24 24"><path d="M6.6 10.8a15.1 15.1 0 0 0 6.6 6.6l2.2-2.2c.3-.3.7-.4 1-.2 1.1.4 2.3.6 3.6.6.6 0 1 .4 1 1V20c0 .6-.4 1-1 1A17 17 0 0 1 3 4c0-.6.4-1 1-1h3.5c.6 0 1 .4 1 1 0 1.3.2 2.5.6 3.6.1.3 0 .7-.2 1z"/></svg>
          555-210-4836
        </li>
        <li>
          <svg viewBox="0 0 24 24"><path d="M7 1h10a2 2 0 0 1 2 2v18a2 2 0 0 1-2 2H7a2 2 0 0 1-2-2V3a2 2 0 0 1 2-2zm0 3v14h10V4z"/></svg>
          555-378-9021
        </li>
        <li>
          <svg viewBox="0 0 24 24"><path d="M2 5h20v14H2zm2 2v.5l8 5 8-5V7z"/></svg>
          Ted@VitaLern.com
        </li>
        <li>
          <svg viewBox="0 0 24 24"><circle cx="12" cy="12" r="10"/></svg>
          www.VitaLern.com
        </li>
      </ul>
    </div>
  </section>
</main>
</body>
</html>
```